Anzeigengestaltung für Handwerksbetrieb
Zielgruppe
Handwerksbetrieb
Maler und Lackierer
Wir möchten mit einem auffälligem und einprägsamen Werbeslogen unsere Bekanntheit in unserer Stadt verstärken. Dieses Design samt Slogan soll künftig alle unsere Werbeaktionen begleiten.
Aufgabenstellung
Der Werbeslogan : 'Wir machen Braunschweig bunter' muss enthalten sein.
Ein optischer Zusammenhang zur Stadt Braunschweig wie z.B. Silouette der Stadt wären wünschenswert.
Gerne bunt und auffallend gestaltet.

```html
<!DOCTYPE html>
<html lang="de">
<head>
<meta charset="UTF-8">
<title>Kessler Malerbetrieb – Wir machen Braunschweig bunter</title>
<link rel="stylesheet" href="https://fonts.googleapis.com/css2?family=Playfair+Display:wght@700;800&family=Montserrat:wght@700&display=swap">
<style>
  :root {
    --brand-red: #7d1820;
    --gold: #cdb27a;
    --white: #ffffff;
    --black: #000000;
    --night-blue: #1b3fa8;
    --violet: #6a2bb8;
    --magenta: #e0247f;
    --glow-green: #2fae7e;
    --amber: #f0b84a;
  }
  * { margin: 0; padding: 0; box-sizing: border-box; }
  html, body { width: 1200px; height: 1200px; overflow: hidden; background: var(--black); }
  .ad {
    position: relative;
    width: 1200px;
    height: 1200px;
    background: var(--black);
    overflow: hidden;
  }
  .skyline-scene {
    position: absolute;
    inset: 0 0 auto 0;
    width: 1200px;
    height: 1010px;
  }
  .brand {
    position: absolute;
    left: 60px;
    top: 95px;
    width: 420px;
    display: flex;
    flex-direction: column;
    align-items: center;
    gap: 30px;
  }
  .brand-mark {
    width: 80px;
    height: 80px;
    background: var(--brand-red);
  }
  .brand-name {
    font-family: "Playfair Display", serif;
    font-weight: 700;
    font-size: 44px;
    line-height: 1.1;
    color: var(--gold);
    text-align: center;
  }
  .slogan {
    position: absolute;
    left: 0;
    right: 0;
    top: 730px;
    text-align: center;
    font-family: "Playfair Display", serif;
    font-weight: 800;
    color: var(--white);
  }
  .slogan-line { display: block; font-size: 80px; line-height: 1.2; }
  .slogan-city { display: block; font-size: 118px; line-height: 1.1; color: var(--gold); letter-spacing: 1px; }
  .contact-bar {
    position: absolute;
    left: 0;
    bottom: 0;
    width: 1200px;
    height: 120px;
    background: var(--brand-red);
    display: flex;
    align-items: center;
    justify-content: center;
    gap: 40px;
    font-family: "Montserrat", sans-serif;
    font-weight: 700;
    font-size: 22px;
    color: var(--white);
  }
  .contact-item { display: flex; align-items: center; gap: 16px; }
  .contact-icon { width: 36px; height: 36px; flex: none; }
</style>
</head>
<body>
<main class="ad">
  <svg class="skyline-scene" viewBox="0 0 1200 1010" xmlns="http://www.w3.org/2000/svg">
    <defs>
      <linearGradient id="nightGlow" x1="0" y1="0" x2="0" y2="1">
        <stop offset="0" stop-color="var(--night-blue)"/>
        <stop offset="0.35" stop-color="var(--violet)"/>
        <stop offset="0.6" stop-color="var(--magenta)"/>
        <stop offset="0.8" stop-color="var(--glow-green)"/>
        <stop offset="1" stop-color="var(--black)"/>
      </linearGradient>
      <radialGradient id="warmLights" cx="0.3" cy="0.75" r="0.5">
        <stop offset="0" stop-color="var(--amber)" stop-opacity="0.55"/>
        <stop offset="1" stop-color="var(--amber)" stop-opacity="0"/>
      </radialGradient>
    </defs>
    <g role="img" aria-label="Bunte, leuchtende Stadtsilhouette bei Nacht mit Lichtern und Spiegelung am Wasser">
      <rect width="1200" height="1010" fill="url(#nightGlow)"/>
      <rect width="1200" height="1010" fill="url(#warmLights)"/>
    </g>
    <path class="header-edge" d="M0,0 H800 C660,0 650,150 580,270 C510,390 430,440 0,440 Z" fill="var(--brand-red)"/>
    <path class="header-panel" d="M0,0 H740 C615,5 600,140 540,250 C480,360 415,425 0,425 Z" fill="var(--white)"/>
  </svg>

  <div class="brand">
    <div class="brand-mark"></div>
    <div class="brand-name">Kessler Malerbetrieb</div>
  </div>

  <h1 class="slogan">
    <span class="slogan-line">Wir machen</span>
    <span class="slogan-city">BRAUNSCHWEIG</span>
    <span class="slogan-line">bunter</span>
  </h1>

  <footer class="contact-bar">
    <div class="contact-item">
      <svg class="contact-icon" viewBox="0 0 36 36" aria-hidden="true">
        <circle cx="18" cy="18" r="18" fill="var(--white)"/>
        <g fill="none" stroke="var(--brand-red)" stroke-width="2">
          <circle cx="18" cy="18" r="10"/>
          <ellipse cx="18" cy="18" rx="4.5" ry="10"/>
          <line x1="8" y1="18" x2="28" y2="18"/>
          <line x1="10" y1="13" x2="26" y2="13"/>
          <line x1="10" y1="23" x2="26" y2="23"/>
        </g>
      </svg>
      <span>www.malerbetriebkessler.example</span>
    </div>
    <div class="contact-item">
      <svg class="contact-icon" viewBox="0 0 36 36" aria-hidden="true">
        <circle cx="18" cy="18" r="18" fill="var(--white)"/>
      </svg>
      <span>social.example/malerbetriebkessler/</span>
    </div>
  </footer>
</main>
</body>
</html>
```